Design an Outstanding flyer for my company.

I need a flyer designed for our window tinting company based in Brisbane Queensland Australia. The flyer will be targeting Home tinting. We also do mobile car tinting. Something in regards to this could be incorporated into the flyer as well.
I want it to be 2 sided DL size. Black background.
It really needs to Pop, and be a real attention getter.
It needs to be easy to read.
I have provided a mock up with the info on it from our marketing company. It will need a spellcheck etc to make sure everything is correct.
Everything about it can be changed however you like.
I have also included the company logo.

Lets see what you've got!

Target Market(s)

Home Owners

Industry/Entity Type

Home Improvement

Font styles to use
Other font styles liked:
• Duan Penh

Requirements
Must have
• All the information on the mock up. Clear and easy to read.
• Must Stand Out!

```html
<!DOCTYPE html>
<html lang="en">
<head>
<meta charset="utf-8">
<title>Brightline Window Tinting – DL Flyer</title>
<link href="https://fonts.googleapis.com/css2?family=Source+Sans+3:wght@400;600;700&family=Roboto+Condensed:wght@300&display=swap" rel="stylesheet">
<style>
  :root {
    --backdrop: #e6e6e6;
    --ink: #0d0d0d;
    --black: #050505;
    --yellow-hi: #f3e63e;
    --yellow-lo: #d8b92a;
    --yellow-edge: #c9a925;
    --gold: #d9bd2c;
    --white: #ffffff;
  }
  * { box-sizing: border-box; margin: 0; padding: 0; }
  html, body { width: 1200px; height: 1200px; overflow: hidden; }
  body {
    background: var(--backdrop);
    font-family: "Source Sans 3", "Myriad Pro", Arial, sans-serif;
    position: relative;
  }
  .flyer {
    position: absolute;
    top: 116px;
    width: 457px;
    height: 960px;
    background: radial-gradient(ellipse at 50% 72%, #262626 0%, var(--black) 60%);
    overflow: hidden;
    box-shadow: 1px 2px 4px rgba(0,0,0,.35);
  }
  .flyer--front { left: 126px; }
  .flyer--back  { left: 622px; }

  .flyer__header {
    position: absolute; left: 0; top: 0; width: 100%; height: 268px;
    background: radial-gradient(ellipse at 50% 10%, var(--yellow-hi) 0%, var(--yellow-lo) 100%);
  }
  .flyer__headline { position: absolute; left: 0; top: 0; width: 100%; height: 100%; }
  .flyer__headline text { font-weight: 700; fill: var(--ink); font-family: "Source Sans 3", Arial, sans-serif; }

  .flyer__rule { position: absolute; left: 0; top: 268px; width: 100%; height: 8px; background: var(--black); }

  .flyer__photo {
    position: absolute; left: 0; top: 276px; width: 100%; height: 330px;
    background: linear-gradient(100deg, #7f9a73 0%, #a6b99a 35%, #6f8a63 55%, #2c2c2c 78%, #1a1a1a 100%);
  }

  .flyer__backfield {
    position: absolute; left: 0; top: 0; width: 100%; height: 620px;
    background: radial-gradient(ellipse at 50% 28%, var(--yellow-hi) 0%, #e6cf31 55%, var(--yellow-lo) 100%);
  }

  .flyer__house { position: absolute; left: 0; top: 470px; width: 457px; height: 200px; }

  .reasons__title {
    position: absolute; left: 0; top: 112px; width: 100%;
    text-align: center; font-weight: 700; color: var(--ink);
    font-size: 34px; line-height: 42px; letter-spacing: .2px;
  }
  .reasons__list {
    position: absolute; left: 26px; right: 22px; top: 247px;
    text-align: center; text-transform: uppercase; color: var(--ink);
    font-size: 13.6px; line-height: 20.2px; font-weight: 400;
  }

  .cta {
    position: absolute; left: 0; top: 625px; width: 100%;
    text-align: center; color: var(--white); font-weight: 600;
    font-size: 28.5px; line-height: 30px; letter-spacing: -.2px;
  }
  .cta__accent { color: var(--gold); }

  .contact {
    position: absolute; left: 48px; top: 700px; width: 380px;
    color: var(--white);
  }
  .contact__row { display: flex; align-items: baseline; height: 48px; }
  .contact__label {
    font-family: "Roboto Condensed", "Arial Narrow", sans-serif; font-weight: 300;
    font-size: 42px; width: 74px; letter-spacing: -1px;
  }
  .contact__colon { font-weight: 700; font-size: 40px; width: 22px; }
  .contact__number { font-weight: 700; font-size: 45px; letter-spacing: .5px; }

  .brand {
    position: absolute; left: 32px; top: 826px; width: 400px; height: 100px;
    display: flex; align-items: center; gap: 20px;
  }
  .brand__dot { width: 78px; height: 78px; border-radius: 50%; background: var(--gold); flex: none; }
  .brand__name {
    color: var(--white); font-weight: 700; font-size: 34px; line-height: 36px; letter-spacing: 1px;
  }
</style>
</head>
<body>

  <!-- Front side -->
  <section class="flyer flyer--front">
    <div class="flyer__header">
      <svg class="flyer__headline" viewBox="0 0 457 268" aria-label="Keep heat out. Block 99.9% UV rays. Save money. Increase privacy.">
        <text x="22" y="88" font-size="60" textLength="412" lengthAdjust="spacingAndGlyphs">KEEP HEAT OUT</text>
        <text x="22" y="138" font-size="45" textLength="412" lengthAdjust="spacingAndGlyphs">BLOCK 99.9% UV RAYS</text>
        <text x="22" y="206" font-size="66" textLength="412" lengthAdjust="spacingAndGlyphs">SAVE MONEY</text>
        <text x="22" y="256" font-size="48" textLength="412" lengthAdjust="spacingAndGlyphs">INCREASE PRIVACY</text>
      </svg>
    </div>
    <div class="flyer__rule"></div>
    <div class="flyer__photo" role="img" aria-label="Photo of an installer applying tint film to a home window overlooking trees"></div>

    <svg class="flyer__house" viewBox="0 0 457 200" aria-hidden="true">
      <path d="M0 118 L226 22 L398 98 L398 52 Q398 46 404 46 L457 46 L457 200 L0 200 Z" fill="#050505"/>
      <path d="M0 118 L226 22 L398 98 L398 52 Q398 46 404 46 L457 46" fill="none" stroke="#d9bd2c" stroke-width="7" stroke-linejoin="round"/>
    </svg>

    <p class="cta"><span class="cta__accent">CALL</span> BRISBANE’S LEADER IN<br>HOME WINDOW TINTING <span class="cta__accent">NOW</span></p>

    <div class="contact">
      <div class="contact__row"><span class="contact__label">TEL</span><span class="contact__colon">:</span><span class="contact__number">07 3100 4827</span></div>
      <div class="contact__row"><span class="contact__label">SMS</span><span class="contact__colon">:</span><span class="contact__number">0400 582 116</span></div>
    </div>

    <div class="brand">
      <span class="brand__dot"></span>
      <span class="brand__name">BRIGHTLINE<br>WINDOW TINTING</span>
    </div>
  </section>

  <!-- Back side -->
  <section class="flyer flyer--back">
    <div class="flyer__backfield"></div>

    <h2 class="reasons__title">20 REASONS WHY<br>HOME WINDOW TINTING<br>IS PERFECT FOR YOU.</h2>
    <p class="reasons__list">Reduce glare. Reduce energy costs. Control the amount of light entering your home. Reduce carbon footprint. Make home more beautiful. Eliminate home hot spots. Protect against broken glass. Regulate energy. Protects upholstery. Improve effectiveness of roof insulation. Improve health. Reduces interior floor fading. Eliminate need for blinds. Strengthen your windows. Insulate in winter. Affordable.</p>

    <svg class="flyer__house" viewBox="0 0 457 200" aria-hidden="true">
      <path d="M0 118 L226 22 L398 98 L398 52 Q398 46 404 46 L457 46 L457 200 L0 200 Z" fill="#050505"/>
      <path d="M0 118 L226 22 L398 98 L398 52 Q398 46 404 46 L457 46" fill="none" stroke="#c9a925" stroke-width="7" stroke-linejoin="round"/>
    </svg>

    <p class="cta"><span class="cta__accent">CALL</span> BRISBANE’S LEADER IN<br>HOME WINDOW TINTING <span class="cta__accent">NOW</span></p>

    <div class="contact">
      <div class="contact__row"><span class="contact__label">TEL</span><span class="contact__colon">:</span><span class="contact__number">07 3100 4827</span></div>
      <div class="contact__row"><span class="contact__label">SMS</span><span class="contact__colon">:</span><span class="contact__number">0400 582 116</span></div>
    </div>

    <div class="brand">
      <span class="brand__dot"></span>
      <span class="brand__name">BRIGHTLINE<br>WINDOW TINTING</span>
    </div>
  </section>

</body>
</html>
```